Business Card Needed for Tend A Patron card should be modern looking with black backgroun

We need a business card designed for a company called Tend A Patron. The business card should have a black background and use our exact logo which is attached. The contact information should be green font. We have additional logo files if needed. The business card should include our logo, our slogan and our contact information.

Target Market(s)

Sales Professionals

Industry/Entity Type

Business

Contact Information for Business Card

Use the information on our website www.tendapatron.example for contact information. The card should also have our slogan "Let us help you plant your referral seed.."

Requirements
Must have
• Black Background with Green Logo and Font

```html
<!DOCTYPE html>
<html lang="en">
<head>
<meta charset="utf-8">
<title>Tend A Patron — Business Card</title>
<link rel="stylesheet" href="https://fonts.googleapis.com/css2?family=Fira+Sans:wght@300;400&display=swap">
<style>
  :root {
    --page: #ffffff;
    --card: #000000;
    --bleed: #e0454f;
    --safe: #4a4a4a;
    --panel: #141414;
    --globe: #262626;
    --green: #22b24c;
    --white: #ffffff;
  }
  html, body {
    margin: 0;
    padding: 0;
    width: 1200px;
    height: 1000px;
    overflow: hidden;
    background: var(--page);
  }
  .canvas {
    position: relative;
    width: 1200px;
    height: 1000px;
    font-family: "Fira Sans", Arial, sans-serif;
  }
  .card {
    position: absolute;
    left: 98px;
    top: 176px;
    width: 1012px;
    height: 652px;
    background: var(--card);
    outline: 1px solid var(--bleed);
  }
  .safe-line {
    position: absolute;
    left: 22px;
    top: 20px;
    width: 968px;
    height: 610px;
    border: 1px solid var(--safe);
    box-sizing: border-box;
  }
  .brand-name {
    position: absolute;
    left: 70px;
    top: 328px;
    width: 370px;
    text-align: center;
    color: var(--white);
    font-weight: 400;
    font-size: 41px;
    letter-spacing: 1px;
    margin: 0;
  }
  .contact-panel {
    position: absolute;
    left: 473px;
    top: 126px;
    width: 472px;
    height: 336px;
    background: var(--panel);
    overflow: hidden;
  }
  .globe-backdrop {
    position: absolute;
    left: 190px;
    top: 10px;
    width: 340px;
    height: 340px;
    border-radius: 50%;
    background: radial-gradient(circle at 45% 40%, var(--globe), var(--panel) 72%);
  }
  .panel-rule {
    position: absolute;
    top: 115px;
    width: 2px;
    height: 360px;
    background: var(--white);
  }
  .panel-rule.left { left: 470px; }
  .panel-rule.right { left: 946px; }
  .contact-icon {
    position: absolute;
    left: 496px;
    width: 56px;
    height: 56px;
  }
  .contact-icon.address { top: 172px; }
  .contact-icon.reach { top: 353px; }
  .contact-block {
    position: absolute;
    left: 570px;
    max-width: 366px;
    margin: 0;
    color: var(--green);
    font-weight: 300;
    font-size: 30px;
    line-height: 40.5px;
    letter-spacing: -0.2px;
    white-space: nowrap;
  }
  .contact-block.address { top: 144px; }
  .contact-block.reach { top: 325px; }
  .slogan-band {
    position: absolute;
    left: 0;
    top: 553px;
    width: 1012px;
    height: 52px;
    background: var(--green);
    color: var(--white);
    font-weight: 300;
    font-size: 33px;
    line-height: 52px;
    text-align: center;
    margin: 0;
  }
</style>
</head>
<body>
<div class="canvas">
  <section class="card">
    <div class="safe-line"></div>

    <h1 class="brand-name">Tend A Patron</h1>

    <div class="contact-panel">
      <div class="globe-backdrop" role="img" aria-label="Faint world map globe behind the contact details"></div>
    </div>
    <div class="panel-rule left"></div>
    <div class="panel-rule right"></div>

    <svg class="contact-icon address" viewBox="0 0 56 56" aria-hidden="true">
      <circle cx="28" cy="28" r="25.5" fill="none" stroke="var(--green)" stroke-width="4"/>
      <path d="M14 29 L28 16 L42 29 Z" fill="var(--green)"/>
      <rect x="18" y="29" width="20" height="12" fill="var(--green)"/>
    </svg>
    <p class="contact-block address">Tend A Patron - LLC<br>P.O. Box 218<br>Fernbrook, MD 20990</p>

    <svg class="contact-icon reach" viewBox="0 0 56 56" aria-hidden="true">
      <circle cx="28" cy="28" r="25.5" fill="none" stroke="var(--green)" stroke-width="4"/>
      <rect x="17" y="14" width="22" height="28" rx="2" fill="var(--green)"/>
      <rect x="15" y="18" width="3" height="3" fill="var(--card)"/>
      <rect x="15" y="26" width="3" height="3" fill="var(--card)"/>
      <rect x="15" y="34" width="3" height="3" fill="var(--card)"/>
      <circle cx="29" cy="24" r="4" fill="var(--card)"/>
      <path d="M22 37 Q29 27 36 37 Z" fill="var(--card)"/>
    </svg>
    <p class="contact-block reach">123 XXX 456(Dummy)<br>mo@tendapatron.example<br>ev@tendapatron.example</p>

    <p class="slogan-band">Let us help you plant your referral seed</p>
  </section>
</div>
</body>
</html>
```